Business Card- Can you make it cool vs boring!

Need a refresh on my business card! Want it to be modern but simple, classic and a pop of coolness! we do senior living and it is boring. but that doesn't mean our business card have to look boring! Open to two sided cards. our website is www.Bruvel-HQ.com

Target Market(s)

capital market

Industry/Entity Type

senior housing/ real estate

Contact Information for Business Card

logo/ name/ cell/ address/ www.Bruvel-HQ.com/ space for a QR code

Requirements
Must have
• maybe a QR code (do not make prominent I may not use the QR so design where it can be taken out) that link to more about us/ landing page. needs to be modern but clean
Should not have
• clip art or script

```html
<!DOCTYPE html>
<html lang="en">
<head>
<meta charset="utf-8">
<title>Bruvel Living – Business Card</title>
<link rel="stylesheet" href="https://fonts.googleapis.com/css2?family=Poppins:wght@400;500;600&display=swap">
<style>
  :root {
    --backdrop: #2b2e33;
    --rust: #b1522a;
    --white: #ffffff;
    --silver: #a9a9ab;
    --ink-rust: #b1522a;
  }
  * { margin: 0; padding: 0; box-sizing: border-box; }
  html, body { width: 1200px; height: 985px; overflow: hidden; }
  body {
    background: var(--backdrop);
    font-family: "Poppins", sans-serif;
    position: relative;
  }
  .card {
    position: absolute;
    width: 700px;
    height: 400px;
    border-radius: 24px;
    overflow: hidden;
    background: var(--rust);
    box-shadow: 0 14px 30px rgba(0,0,0,0.35);
  }
  .card--front { left: 250px; top: 70px; }
  .card--back  { left: 250px; top: 515px; }

  .front-shape { position: absolute; inset: 0; }

  .brand-name {
    position: absolute;
    font-family: "Poppins", sans-serif;
    font-weight: 500;
    white-space: nowrap;
  }
  .card--front .brand-name {
    left: 34px; top: 168px;
    font-size: 30px;
    color: var(--ink-rust);
  }
  .card--back .brand-name {
    left: 0; right: 0; top: 168px;
    text-align: center;
    font-size: 48px;
    color: var(--white);
  }

  .contact {
    position: absolute;
    left: 345px; top: 86px;
    color: var(--white);
  }
  .contact__name { font-size: 27px; font-weight: 600; line-height: 1.1; }
  .contact__role { font-size: 12px; font-weight: 400; margin-bottom: 12px; }
  .contact__address { font-size: 15px; line-height: 1.35; margin-bottom: 10px; }
  .contact__list { list-style: none; font-size: 15px; line-height: 1.5; }
  .contact__list li { display: flex; align-items: center; gap: 8px; }
  .contact__icon {
    width: 14px; height: 14px; border-radius: 50%;
    background: var(--white);
    display: inline-flex; align-items: center; justify-content: center;
    flex: none;
  }
  .social {
    display: flex; gap: 6px; margin-top: 12px;
  }
  .social__square {
    width: 20px; height: 20px;
    background: var(--white);
    border-radius: 2px;
  }
</style>
</head>
<body>

<section class="card card--front" aria-label="Business card front">
  <svg class="front-shape" width="700" height="400" viewBox="0 0 700 400" aria-hidden="true">
    <path d="M0 0 H300 C350 130 330 300 200 400 H0 Z" fill="#a9a9ab"/>
    <path d="M0 0 H290 C335 120 300 290 150 372 C100 390 40 392 0 390 Z" fill="#ffffff"/>
  </svg>
  <div class="brand-name">Bruvel Living</div>

  <div class="contact">
    <div class="contact__name">Martin K Ellery</div>
    <div class="contact__role">CEO</div>
    <div class="contact__address">4107 Cedarbrook Lane<br>Suite #1204</div>
    <ul class="contact__list">
      <li>
        <span class="contact__icon">
          <svg width="8" height="8" viewBox="0 0 10 10"><path d="M2 1 L4 1 L5 3.5 L3.8 4.5 C4.5 6 5 6.5 6.5 7.2 L7.5 6 L10 7 L10 9 C5 9.5 0.5 5 1 1 Z" fill="#b1522a"/></svg>
        </span>(555) 014-27380
      </li>
      <li>
        <span class="contact__icon">
          <svg width="8" height="8" viewBox="0 0 10 10"><rect x="1" y="2.5" width="8" height="5.5" fill="none" stroke="#b1522a" stroke-width="1.2"/><path d="M1 2.5 L5 5.5 L9 2.5" fill="none" stroke="#b1522a" stroke-width="1.2"/></svg>
        </span>info@bruvelmail.com
      </li>
      <li>
        <span class="contact__icon">
          <svg width="8" height="8" viewBox="0 0 10 10"><circle cx="5" cy="5" r="4" fill="none" stroke="#b1522a" stroke-width="1.2"/><path d="M1 5 H9 M5 1 V9" stroke="#b1522a" stroke-width="1"/></svg>
        </span>www.Bruvel-HQ.com
      </li>
    </ul>
    <div class="social" aria-label="Social profiles">
      <span class="social__square"></span>
      <span class="social__square"></span>
      <span class="social__square"></span>
    </div>
  </div>
</section>

<section class="card card--back" aria-label="Business card back">
  <div class="brand-name">Bruvel Living</div>
</section>

</body>
</html>
```